PlumEcho Social Sharing Platform Needs a Redesign (2 pages / Design only)

PlumEcho is a popular social sharing platform for bloggers and marketers. The site has been quite popular for a few years now, but the site's design is looking quite dated. We're looking for a brand new design to give the service a facelift.

We are looking for a modern and fresh design that keeps all the existing functionality intact. Would prefer designs that incorporate the color blue in them.

We would like the two attached screenshots to be redesigned and submitted - using he same content. Please do not submit a redesign of the front page (non-logged in version). Redesign the 2 attached pages only, and the final deliverable is these two pages as layered PSD files.

Target Market(s)

bloggers, internet marketers

Industry/Entity Type

Social

Number of Pages Required

2 page

Requirements
Must have
• All existing functionality must be intact as seen from the screenshots.
Should not have
• Please do not submit designs based on existing front page (non-logged in version). Use attached screenshots (file 1 and 2) as a guide of existing functionality.

```html
<!DOCTYPE html>
<html lang="en">
<head>
<meta charset="utf-8">
<title>PlumEcho – Dashboard and Submit Chirp</title>
<link href="https://fonts.googleapis.com/css2?family=Open+Sans:ital,wght@0,300;0,400;0,600;0,700;1,400&display=swap" rel="stylesheet">
<style>
:root{
  --blue:#1a5fa8;
  --blue-dark:#154f8e;
  --link:#1b6fc2;
  --ink:#333;
  --muted:#777;
  --line:#d9d9d9;
  --panel:#f2f5f9;
  --slate:#3b4656;
  --footer:#4a4a4a;
  --notice:#f6ecb8;
  --notice-line:#e4cf7a;
  --orange:#f0a030;
  --green:#6db33f;
  --red:#e04343;
  --lime:#a6c733;
  --stage:#000;
}
*{box-sizing:border-box;margin:0;padding:0}
html,body{width:1200px;height:954px;overflow:hidden;background:var(--stage);font-family:"Open Sans",Arial,sans-serif;color:var(--ink)}
.canvas{position:relative;width:1200px;height:954px}
.page{position:absolute;top:63px;width:522px;height:834px;background:#fff;overflow:hidden;font-size:8px}
.page--dashboard{left:56px}
.page--submit{left:628px;width:521px}
.abs{position:absolute}

/* header */
.topbar{position:absolute;left:0;top:0;width:100%;height:30px;background:var(--blue)}
.brand{position:absolute;left:10px;top:0;width:134px;height:30px;background:#fff;display:flex;align-items:center;gap:6px;padding-left:8px}
.brand-mark{width:12px;height:12px;background:var(--blue)}
.brand-name{font-size:17px;font-weight:700;color:var(--blue);letter-spacing:-.3px}
.logout{position:absolute;left:339px;top:10px;color:#fff;font-size:8px;font-weight:600;display:flex;align-items:center;gap:4px}
.user{position:absolute;left:410px;top:4px;display:flex;align-items:center;gap:10px;color:#fff;font-size:8px}
.user-photo{width:22px;height:22px;border-radius:50%;background:linear-gradient(#d8b79a,#9a7a66);border:2px solid #fff}
.user-bar{position:absolute;left:410px;top:27px;width:24px;height:3px;background:var(--green)}

/* nav */
.mainnav{position:absolute;left:7px;right:7px;top:36px;height:27px;display:flex;justify-content:space-between;align-items:center}
.mainnav a{font-size:8.6px;color:#333;text-decoration:none;text-transform:uppercase;letter-spacing:.1px;padding:5px 0}
.mainnav a.is-active{color:var(--blue);border-bottom:2px solid var(--blue)}

/* sidebar */
.credits{position:absolute;left:392px;top:71px;width:122px;height:98px;background:var(--blue);color:#fff;text-align:center;padding-top:14px}
.credits-total{font-size:22px;font-weight:300;line-height:24px}
.credits-label{font-size:9px;line-height:13px}
.credits-cta{font-size:9px;line-height:13px}
.credits-cta b{font-weight:700}
.credits-action{font-size:11px;font-weight:600;line-height:14px}
.engage{position:absolute;left:392px;top:183px;width:122px;height:159px;background:var(--panel);text-align:center;padding-top:8px}
.engage h3{font-size:8px;font-weight:600;line-height:10px;color:#444;padding:0 6px}
.engage-grid{display:grid;grid-template-columns:repeat(3,37px);justify-content:center;row-gap:6px;margin-top:10px}
.member-s{display:flex;flex-direction:column;align-items:center}
.placeholder{width:24px;height:24px;background:#d7d7d7;border:1px solid #c8c8c8}
.member-s span{font-size:6px;color:#444;margin-top:3px}
.btn-follow{display:inline-block;width:24px;height:7px;line-height:7px;background:#1d63ab;color:#fff;font-size:5.5px;font-weight:600;text-align:center;margin-top:2px}
.sites{position:absolute;left:392px;top:355px;width:122px;height:325px;border:1px solid var(--line)}
.sites h3{background:var(--footer);color:#fff;font-size:8px;font-weight:400;text-align:center;height:17px;line-height:17px}
.site{padding:6px 8px 0}
.site h4{font-size:7.5px;font-weight:600;color:#333;line-height:10px}
.site-shot{width:104px;height:78px;margin-top:5px}
.shot-a{background:linear-gradient(160deg,#2c3e5a,#5779a3 55%,#b9c6d6)}
.shot-b{background:linear-gradient(170deg,#e8eef6,#ef7d3a 45%,#3a78c2)}
.site p{font-size:6.4px;line-height:8.5px;color:#444;margin-top:4px}
.site + .site{border-top:1px solid var(--line);margin-top:7px}

.backtop{position:absolute;left:469px;top:757px;width:53px;height:27px;background:var(--blue);color:#fff;font-size:6.5px;text-align:center;line-height:8px;padding-top:5px}
.page--submit .backtop{left:468px}
.footer{position:absolute;left:0;top:784px;width:100%;height:50px;background:var(--footer);color:#ddd;text-align:center;font-size:6.5px;padding-top:15px;line-height:11px}

/* dashboard */
.notice{position:absolute;left:7px;top:72px;width:375px;height:26px;background:var(--notice);border:1px solid var(--notice-line);display:flex;align-items:center;gap:8px;padding-left:6px;font-size:8.6px;color:#8a6d1c}
.notice-icon{width:17px;height:17px;background:var(--orange);display:flex;align-items:center;justify-content:center}
.featured{position:absolute;left:7px;top:113px;width:375px;height:171px;border:1px solid var(--blue)}
.featured h2{height:24px;background:var(--blue);color:#fff;font-size:8.6px;font-weight:600;line-height:24px;padding-left:10px}
.featured-grid{display:grid;grid-template-columns:repeat(8,44.5px);row-gap:10px;padding:10px 0 0 4px}
.member{display:flex;flex-direction:column;align-items:center}
.member-photo{width:32px;height:32px}
.member span{font-size:6px;color:#333;margin-top:2px}
.member .btn-follow{width:22px}
.btn-buy{background:var(--lime)}
.c1{background:#3f8fcf}.c2{background:#8d6e5c}.c3{background:#c88e6a}.c4{background:linear-gradient(135deg,#f6b0c5,#9fd0f0,#f7da6e)}
.c5{background:#a88670}.c6{background:#6a4a3c}.c7{background:#b07f66}.c8{background:#5a4236}.c9{background:#d2d2d2}

.filter{position:absolute;left:7px;top:300px;width:375px;height:87px;background:var(--slate)}
.filter-box{position:absolute;left:16px;top:15px;width:343px;height:57px;background:#fff;padding:8px 8px 0 15px}
.filter-row{display:flex;align-items:center;gap:6px}
.filter-row label{font-weight:700;font-size:7.5px;width:46px}
.select{height:14px;border:1px solid #ccc;font-size:7px;line-height:12px;padding:0 5px;display:flex;justify-content:space-between;align-items:center;color:#444}
.select::after{content:"";border:2.5px solid transparent;border-top:3px solid #888;margin-top:3px}
.search{margin-top:7px;height:16px;border:1px solid #ccc;display:flex;font-size:7px;color:#666}
.search span{flex:1;padding:2px 6px}
.search i{width:18px;background:#bbb;display:flex;align-items:center;justify-content:center}

.chirp{position:absolute;left:7px;width:375px}
.chirp-photo{position:absolute;left:1px;top:2px;width:31px;height:31px;border:1px solid #ddd}
.chirp-card{position:absolute;left:40px;top:0;width:335px;border:1px solid var(--line);background:#f6f6f6}
.chirp-card.is-featured{border-color:#4c8fd1;background:#f4f8fc}
.chirp-body{padding:18px 20px 0;font-size:7.3px;line-height:12px;color:#333;height:67px;background:#fff}
.chirp-card.is-featured .chirp-body{background:#f4f8fc}
.chirp-body b{font-weight:700}
.chirp-body a{color:var(--link);text-decoration:none}
.chirp-actions{border-top:1px solid var(--line);height:32px;display:flex;align-items:center;padding-left:20px;gap:9px;font-size:6.6px;color:#1b6fc2;background:#fff}
.chirp-card.is-featured .chirp-actions{background:#f4f8fc}
.chirp-actions .act{display:flex;align-items:center;gap:3px}
.counter{display:flex;align-items:center;gap:2px;font-size:6px;color:#555}
.counter b{display:inline-block;height:10px;line-height:10px;padding:0 3px;background:#3b5a98;color:#fff;font-weight:600;font-size:6px}
.counter.alt b{background:#fff;color:var(--red);border:1px solid #ddd}
.counter em{font-style:normal;border:1px solid #ccc;padding:0 2px;height:10px;line-height:9px}
.spacer{flex:1}
.featured-tab{position:absolute;left:32px;top:43px;width:14px;height:57px;background:#3d86cf;color:#fff;font-size:6.5px;writing-mode:vertical-rl;transform:rotate(180deg);text-align:center;line-height:14px}
.spinner{position:absolute;left:203px;top:753px}

/* submit */
.form{position:absolute;left:9px;top:76px;width:373px;font-size:7.7px;color:#333}
.form h2{font-size:8.6px;font-weight:700;line-height:12px}
.form .note{font-style:italic;font-size:7.3px;line-height:10px;margin-top:2px}
.field-label{position:absolute;left:0;font-size:7.7px}
.input{position:absolute;left:0;width:110px;height:16px;border:1px solid #ccc;font-size:7.3px;padding:2px 5px}
.textarea{position:absolute;left:0;top:62px;width:373px;height:44px;border:1px solid #ccc}
.hint{position:absolute;font-size:6.5px;color:#777}
.aside-text{position:absolute;left:117px;font-size:7.5px}
.check{position:absolute;left:0;display:flex;align-items:center;gap:6px;font-size:7.5px}
.check i{width:8px;height:8px;border:1px solid #888;display:flex;align-items:center;justify-content:center}
.btn-submit{position:absolute;left:0;top:370px;width:58px;height:22px;background:var(--blue);color:#fff;font-size:8.6px;font-weight:700;text-align:center;line-height:22px;letter-spacing:.3px}
.post-note{position:absolute;left:0;top:402px;width:373px;font-size:7.5px;line-height:11px}
.post-note a{color:var(--link);text-decoration:none}
.recent-title{position:absolute;left:0;top:436px;font-size:9.4px;font-weight:700}
.recent{position:absolute;left:9px;top:531px;width:373px;height:238px;border:1px solid var(--blue)}
.recent-head{height:22px;background:var(--blue);color:#fff;font-size:7.7px;font-weight:600;display:flex;line-height:22px}
.recent-head span:first-child{width:309px;padding-left:7px;border-right:1px solid #fff}
.recent-head span:last-child{padding-left:7px}
.post{position:relative;margin:0 11px;height:63px;border-bottom:1px solid var(--line);padding-top:9px;font-size:7.2px;line-height:12px}
.post a{color:var(--link);text-decoration:none}
.post-stats{display:flex;gap:14px;margin-top:1px;font-size:7px}
.post-stats .red{color:var(--red)}
.post-tools{position:absolute;left:302px;top:10px;display:flex;gap:3px}
.post-tools i{width:14px;height:14px;display:flex;align-items:center;justify-content:center}
.t-edit{background:var(--orange)}.t-add{background:var(--green)}.t-del{background:var(--red)}
.pager{position:absolute;left:10px;top:219px;font-size:7px;display:flex;width:300px}
.pager b{font-weight:700}
.pager .pages{margin-left:46px;color:#888;display:flex;gap:4px}
.pager .pages a{color:var(--link);text-decoration:underline}
.pager .pages span.next{color:#333}
</style>
</head>
<body>
<div class="canvas">

<!-- DASHBOARD -->
<section class="page page--dashboard">
  <header class="topbar">
    <div class="brand"><span class="brand-mark"></span><span class="brand-name">PlumEcho</span></div>
    <div class="logout">Logout
      <svg width="8" height="8" viewBox="0 0 8 8"><rect x="1" y="3.5" width="6" height="4" fill="#fff"/><path d="M2.3 3.5V2.2a1.7 1.7 0 0 1 3.4 0" stroke="#fff" fill="none"/></svg>
    </div>
    <div class="user"><span class="user-photo" role="img" aria-label="Member profile photo"></span>Danmerrow</div>
    <span class="user-bar"></span>
  </header>
  <nav class="mainnav">
    <a class="is-active">Dashboard</a><a>Chirpr Followers</a><a>Submit Chirp</a><a>Activity Summary</a><a>Buy Credots</a><a>Settings</a><a>Affiliates</a>
  </nav>

  <div class="notice">
    <span class="notice-icon"><svg width="11" height="9" viewBox="0 0 11 9"><path d="M1 3h2l5-2.5v8L3 6H1z" fill="#fff"/></svg></span>
    See who won our contest Click here
  </div>

  <div class="featured">
    <h2>Featured Chirp</h2>
    <div class="featured-grid">
      <div class="member"><div class="member-photo c1" role="img" aria-label="Member avatar"></div><span>name here</span><b class="btn-follow">follow</b></div>
      <div class="member"><div class="member-photo c2" role="img" aria-label="Member photo"></div><span>name here</span><b class="btn-follow">follow</b></div>
      <div class="member"><div class="member-photo c3" role="img" aria-label="Member photo"></div><span>name here</span><b class="btn-follow">follow</b></div>
      <div class="member"><div class="member-photo c4" role="img" aria-label="Member avatar graphic"></div><span>name here</span><b class="btn-follow">follow</b></div>
      <div class="member"><div class="member-photo c5" role="img" aria-label="Member photo"></div><span>name here</span><b class="btn-follow">follow</b></div>
      <div class="member"><div class="member-photo c6" role="img" aria-label="Member photo"></div><span>name here</span><b class="btn-follow">follow</b></div>
      <div class="member"><div class="member-photo c7" role="img" aria-label="Member photo"></div><span>name here</span><b class="btn-follow">follow</b></div>
      <div class="member"><div class="member-photo c8" role="img" aria-label="Member photo"></div><span>name here</span><b class="btn-follow">follow</b></div>
      <div class="member"><div class="member-photo c1" role="img" aria-label="Member avatar"></div><span>name here</span><b class="btn-follow">follow</b></div>
      <div class="member"><div class="member-photo c2" role="img" aria-label="Member photo"></div><span>name here</span><b class="btn-follow">follow</b></div>
      <div class="member"><div class="member-photo c3" role="img" aria-label="Member photo"></div><span>name here</span><b class="btn-follow">follow</b></div>
      <div class="member"><div class="member-photo c4" role="img" aria-label="Member avatar graphic"></div><span>name here</span><b class="btn-follow">follow</b></div>
      <div class="member"><div class="member-photo c5" role="img" aria-label="Member photo"></div><span>name here</span><b class="btn-follow">follow</b></div>
      <div class="member"><div class="member-photo c6" role="img" aria-label="Member photo"></div><span>name here</span><b class="btn-follow">follow</b></div>
      <div class="member"><div class="member-photo c7" role="img" aria-label="Member photo"></div><span>name here</span><b class="btn-follow">follow</b></div>
      <div class="member"><div class="member-photo c9" role="img" aria-label="Empty avatar placeholder"></div><span>name here</span><b class="btn-follow btn-buy">buy</b></div>
    </div>
  </div>

  <div class="filter">
    <div class="filter-box">
      <div class="filter-row">
        <label>Oorder by:</label>
        <div class="select" style="width:70px">Most Recent</div>
        <div class="select" style="width:104px">All categories</div>
      </div>
      <div class="search"><span>Search (keyword or Chirpr handle)</span>
        <i><svg width="9" height="9" viewBox="0 0 9 9"><circle cx="3.7" cy="3.7" r="2.7" stroke="#fff" stroke-width="1.2" fill="none"/><path d="M5.7 5.7 8.3 8.3" stroke="#fff" stroke-width="1.3"/></svg></i>
      </div>
    </div>
  </div>

  <article class="chirp" style="top:404px">
    <div class="chirp-photo c2" role="img" aria-label="Member photo"></div>
    <div class="chirp-card">
      <div class="chirp-body"><b>@BlogGrowthPro</b> is offering 35 credits to promote this (Affiliates)<br>Here's how to become a trustworthy affiliate <a>http://deck.sh/4kT2Ba</a> via<br>@DeckShare</div>
      <div class="chirp-actions">
        <span class="act">↻ Report Chirp</span><span class="act">➜ Skip this</span><span class="act">↻ Shedule Rechirp</span>
        <span class="spacer"></span>
        <span class="counter"><b>Like</b><em>11</em></span>
        <span class="counter alt" style="margin:0 20px 0 10px"><b>+1</b><em>6</em></span>
      </div>
    </div>
  </article>

  <article class="chirp" style="top:522px">
    <div class="chirp-photo c3" role="img" aria-label="Member photo"></div>
    <div class="featured-tab">Featured Chirp</div>
    <div class="chirp-card is-featured">
      <div class="chirp-body"><b>@BlogGrowthPro</b> is offering 35 credits to promote this (Affiliates)<br>Here's how to become a trustworthy affiliate <a>http://deck.sh/4kT2Ba</a> via<br>@DeckShare</div>
      <div class="chirp-actions">
        <span class="act">↻ Report Chirp</span><span class="act">➜ Skip this</span><span class="act">↻ Shedule Rechirp</span>
        <span class="spacer"></span>
        <span class="counter"><b>Like</b><em>11</em></span>
        <span class="counter alt" style="margin:0 20px 0 10px"><b>+1</b><em>6</em></span>
      </div>
    </div>
  </article>

  <article class="chirp" style="top:639px">
    <div class="chirp-photo c7" role="img" aria-label="Member photo"></div>
    <div class="chirp-card">
      <div class="chirp-body"><b>@BlogGrowthPro</b> is offering 35 credits to promote this (Affiliates)<br>Here's how to become a trustworthy affiliate <a>http://deck.sh/4kT2Ba</a> via<br>@DeckShare</div>
      <div class="chirp-actions">
        <span class="act">↻ Report Chirp</span><span class="act">➜ Skip this</span><span class="act">↻ Shedule Rechirp</span>
        <span class="spacer"></span>
        <span class="counter"><b>Like</b><em>11</em></span>
        <span class="counter alt" style="margin:0 20px 0 10px"><b>+1</b><em>6</em></span>
      </div>
    </div>
  </article>

  <svg class="spinner" width="16" height="16" viewBox="0 0 16 16" aria-hidden="true">
    <g stroke="#666" stroke-width="2" stroke-linecap="round">
      <path d="M8 1v3" opacity=".9"/><path d="M13 3l-2 2" opacity=".8"/><path d="M15 8h-3" opacity=".7"/><path d="M13 13l-2-2" opacity=".6"/>
      <path d="M8 15v-3" opacity=".5"/><path d="M3 13l2-2" opacity=".4"/><path d="M1 8h3" opacity=".3"/><path d="M3 3l2 2" opacity=".2"/>
    </g>
  </svg>

  <aside>
    <div class="credits"><div class="credits-total">315959</div><div class="credits-label">YOUR CREDITS</div><div class="credits-cta"><b>click here</b> to submit</div><div class="credits-action">A Rechirp</div></div>
    <div class="engage">
      <h3>Engage with other members who have recently shared your chirps</h3>
      <div class="engage-grid">
        <div class="member-s"><i class="placeholder"></i><span>name</span><b class="btn-follow">follow</b></div>
        <div class="member-s"><i class="placeholder"></i><span>name</span><b class="btn-follow">follow</b></div>
        <div class="member-s"><i class="placeholder"></i><span>name</span><b class="btn-follow">follow</b></div>
        <div class="member-s"><i class="placeholder"></i><span>name</span><b class="btn-follow">follow</b></div>
        <div class="member-s"><i class="placeholder"></i><span>name</span><b class="btn-follow">follow</b></div>
        <div class="member-s"><i class="placeholder"></i><span>name</span><b class="btn-follow">follow</b></div>
      </div>
    </div>
    <div class="sites">
      <h3>Featured Websites</h3>
      <div class="site"><h4>Startup Chatter</h4><div class="site-shot shot-a" role="img" aria-label="Website screenshot preview"></div><p>Business resource &amp; tips for Start Ups, SME's &amp; Entrepreneurs. Business experts, for the business community.</p></div>
      <div class="site"><h4>SEO Training &amp; Internet Marketing Blog</h4><div class="site-shot shot-b" role="img" aria-label="Website screenshot preview"></div><p>SEO Training Blog, With Free SEO Tools, Unique Strategies &amp; Free Video Tutorials</p></div>
    </div>
  </aside>

  <div class="backtop">BACK<br>TO TOP</div>
  <footer class="footer">Dashboard &nbsp;|&nbsp; Chirpr Followers &nbsp;|&nbsp; Submit Chirp &nbsp;|&nbsp; Activity Summary &nbsp;|&nbsp; Buy Credots &nbsp;|&nbsp; Settings &nbsp;|&nbsp; Affiliates<br>© 2014. All Rights Reserved</footer>
</section>

<!-- SUBMIT CHIRP -->
<section class="page page--submit">
  <header class="topbar">
    <div class="brand"><span class="brand-mark"></span><span class="brand-name">PlumEcho</span></div>
    <div class="logout">Logout
      <svg width="8" height="8" viewBox="0 0 8 8"><rect x="1" y="3.5" width="6" height="4" fill="#fff"/><path d="M2.3 3.5V2.2a1.7 1.7 0 0 1 3.4 0" stroke="#fff" fill="none"/></svg>
    </div>
    <div class="user"><span class="user-photo" role="img" aria-label="Member profile photo"></span>Danmerrow</div>
    <span class="user-bar"></span>
  </header>
  <nav class="mainnav">
    <a class="is-active">Dashboard</a><a>Chirpr Followers</a><a>Submit Chirp</a><a>Activity Summary</a><a>Buy Credots</a><a>Settings</a><a>Affiliates</a>
  </nav>

  <form class="form">
    <h2>Submit a Chirp</h2>
    <p class="note">Please do not request rechirps for sales pages, direct affiliate links, squeeze pages, homepage links and other overly promotional or low quality content. These will be deleted.</p>
    <span class="field-label" style="top:48px">Chirp (<b>RC@tall_wren</b> will be added automatically to your message)</span>
    <div class="textarea"></div>
    <span class="hint" style="top:112px;left:0">(You have 124 characters left)</span>
    <span class="field-label" style="top:132px">How many credits would you like to offer members to promote this message</span>
    <div class="input" style="top:145px"></div>
    <span class="field-label" style="top:174px">Maximum times to promote</span>
    <div class="input" style="top:186px">0</div><span class="aside-text" style="top:190px">You will spend 0 credits</span>
    <span class="field-label" style="top:216px">Select which Social Networks to allow</span>
    <span class="check" style="top:231px"><i><svg width="6" height="6" viewBox="0 0 6 6"><path d="M.8 3 2.4 4.6 5.3 1" stroke="#333" stroke-width="1.1" fill="none"/></svg></i>Chirpr</span>
    <span class="check" style="top:244px"><i></i>FaceLink</span>
    <span class="check" style="top:257px"><i></i>CirclePlus</span>
    <span class="field-label" style="top:279px">Minimum number of Chirpr followers to promote</span>
    <div class="input" style="top:291px">0</div><span class="aside-text" style="top:295px">100% of members will see this chirp</span>
    <span class="field-label" style="top:324px">Category</span>
    <div class="select abs" style="top:336px;left:0;width:110px;height:16px">Plese Select</div>
    <div class="btn-submit">SUBMIT</div>
    <p class="post-note">This submitted chirp <b>will be posted immediately</b> to your Chirpr timeline. You can change this option by going to the <a>Settings pages</a>.</p>
    <h3 class="recent-title">Most Recently Submitted Chirps</h3>
  </form>

  <div class="recent">
    <div class="recent-head"><span>Posted Chirp</span><span>Actions</span></div>
    <div class="post">Posted 421 days ago for 35 credits (Completed)<br>Top Affiliate Marketing Blogs and News Feeds <a>http://samplewriter.net/top-affiliate-<br>marketing-blogs-news-feeds/</a>
      <div class="post-stats"><a>Rechirps (17)</a><a>Linkes (10)</a><span class="red">Plus Opens (8)</span></div>
      <div class="post-tools"><i class="t-edit"><svg width="7" height="7" viewBox="0 0 7 7"><path d="M1 6 1.3 4.6 4.8 1.1 5.9 2.2 2.4 5.7z" fill="#fff"/></svg></i><i class="t-add"><svg width="7" height="7" viewBox="0 0 7 7"><path d="M3.5 1v5M1 3.5h5" stroke="#fff" stroke-width="1.4"/></svg></i><i class="t-del"><svg width="7" height="7" viewBox="0 0 7 7"><path d="M1.2 1.2l4.6 4.6M5.8 1.2 1.2 5.8" stroke="#fff" stroke-width="1.3"/></svg></i></div>
    </div>
    <div class="post">Posted 421 days ago for 35 credits (Completed)<br>Top Affiliate Marketing Blogs and News Feeds <a>http://samplewriter.net/top-affiliate-<br>marketing-blogs-news-feeds/</a>
      <div class="post-stats"><a>Rechirps (17)</a><a>Linkes (10)</a><span class="red">Plus Opens (8)</span></div>
      <div class="post-tools"><i class="t-edit"><svg width="7" height="7" viewBox="0 0 7 7"><path d="M1 6 1.3 4.6 4.8 1.1 5.9 2.2 2.4 5.7z" fill="#fff"/></svg></i><i class="t-add"><svg width="7" height="7" viewBox="0 0 7 7"><path d="M3.5 1v5M1 3.5h5" stroke="#fff" stroke-width="1.4"/></svg></i><i class="t-del"><svg width="7" height="7" viewBox="0 0 7 7"><path d="M1.2 1.2l4.6 4.6M5.8 1.2 1.2 5.8" stroke="#fff" stroke-width="1.3"/></svg></i></div>
    </div>
    <div class="post">Posted 421 days ago for 35 credits (Completed)<br>Top Affiliate Marketing Blogs and News Feeds <a>http://samplewriter.net/top-affiliate-<br>marketing-blogs-news-feeds/</a>
      <div class="post-stats"><a>Rechirps (17)</a><a>Linkes (10)</a><span class="red">Plus Opens (8)</span></div>
      <div class="post-tools"><i class="t-edit"><svg width="7" height="7" viewBox="0 0 7 7"><path d="M1 6 1.3 4.6 4.8 1.1 5.9 2.2 2.4 5.7z" fill="#fff"/></svg></i><i class="t-add"><svg width="7" height="7" viewBox="0 0 7 7"><path d="M3.5 1v5M1 3.5h5" stroke="#fff" stroke-width="1.4"/></svg></i><i class="t-del"><svg width="7" height="7" viewBox="0 0 7 7"><path d="M1.2 1.2l4.6 4.6M5.8 1.2 1.2 5.8" stroke="#fff" stroke-width="1.3"/></svg></i></div>
    </div>
    <div class="pager"><b>Results</b>&nbsp;1 - 10 of 16 Page<span class="pages">Previous <a>1</a><a>2</a> <span class="next">Next</span></span></div>
  </div>

  <aside>
    <div class="credits"><div class="credits-total">315959</div><div class="credits-label">YOUR CREDITS</div><div class="credits-cta"><b>click here</b> to submit</div><div class="credits-action">A Rechirp</div></div>
    <div class="engage">
      <h3>Engage with other members who have recently shared your chirps</h3>
      <div class="engage-grid">
        <div class="member-s"><i class="placeholder"></i><span>name</span><b class="btn-follow">follow</b></div>
        <div class="member-s"><i class="placeholder"></i><span>name</span><b class="btn-follow">follow</b></div>
        <div class="member-s"><i class="placeholder"></i><span>name</span><b class="btn-follow">follow</b></div>
        <div class="member-s"><i class="placeholder"></i><span>name</span><b class="btn-follow">follow</b></div>
        <div class="member-s"><i class="placeholder"></i><span>name</span><b class="btn-follow">follow</b></div>
        <div class="member-s"><i class="placeholder"></i><span>name</span><b class="btn-follow">follow</b></div>
      </div>
    </div>
    <div class="sites">
      <h3>Featured Websites</h3>
      <div class="site"><h4>Startup Chatter</h4><div class="site-shot shot-a" role="img" aria-label="Website screenshot preview"></div><p>Business resource &amp; tips for Start Ups, SME's &amp; Entrepreneurs. Business experts, for the business community.</p></div>
      <div class="site"><h4>SEO Training &amp; Internet Marketing Blog</h4><div class="site-shot shot-b" role="img" aria-label="Website screenshot preview"></div><p>SEO Training Blog, With Free SEO Tools, Unique Strategies &amp; Free Video Tutorials</p></div>
    </div>
  </aside>

  <div class="backtop">BACK<br>TO TOP</div>
  <footer class="footer">Dashboard &nbsp;|&nbsp; Chirpr Followers &nbsp;|&nbsp; Submit Chirp &nbsp;|&nbsp; Activity Summary &nbsp;|&nbsp; Buy Credots &nbsp;|&nbsp; Settings &nbsp;|&nbsp; Affiliates<br>© 2014. All Rights Reserved</footer>
</section>

</div>
</body>
</html>
```